HALVARO
Zielgruppe
GPS Audio Apps, Entwicklung von Audio-Guides für Draußen
potentielle Auftraggeber: Standortmarketing, Tourismusmarketing, Gemeinden, Kulturinstitutionen
Aufgabenstellung
Layout Briefkopf /Visitenkarte
Text:
Halvaro (HALVARO)
GPS AUDIO APPS
www.halvaro-beispiel.de
Visitenkarte Rückseite: Orte zum Sprechen bringen...
Das PDF zeigt einen ersten Versuch meinerseits, ich bin aber auch für ganz andere Vorschläge offen. Generell stelle ich mir eine schlichte Typographie vor, ohne Icons oder Ähnliches.

```html
<!DOCTYPE html>
<html lang="de">
<head>
<meta charset="utf-8">
<title>Halvaro – Visitenkarte</title>
<link rel="stylesheet" href="https://fonts.googleapis.com/css2?family=Oswald:wght@300&family=Pathway+Gothic+One&family=Alegreya+Sans+SC:wght@400&display=swap">
<style>
  :root {
    --paper: #ffffff;
    --ink: #111111;
    --rule: #9a9a9a;
  }
  html, body {
    margin: 0;
    padding: 0;
    overflow: hidden;
    background: var(--paper);
  }
  .sheet {
    position: relative;
    width: 1200px;
    height: 388px;
    background: var(--paper);
    color: var(--ink);
    overflow: hidden;
  }
  .card-front, .card-back {
    position: absolute;
    top: 0;
    height: 388px;
  }
  .card-front { left: 0; width: 600px; }
  .card-back { left: 601px; width: 599px; }
  .divider {
    position: absolute;
    left: 600px;
    top: 0;
    width: 1px;
    height: 388px;
    background: var(--rule);
  }
  .brand-name {
    position: absolute;
    right: 60px;
    top: 22px;
    margin: 0;
    font-family: "Oswald", sans-serif;
    font-weight: 300;
    font-size: 34px;
    line-height: 1;
    letter-spacing: 4px;
  }
  .service-line {
    position: absolute;
    left: 214px;
    top: 84px;
    margin: 0;
    font-family: "Oswald", sans-serif;
    font-weight: 300;
    font-size: 52px;
    line-height: 1;
    letter-spacing: 4px;
    white-space: nowrap;
  }
  .contact {
    position: absolute;
    left: 10px;
    top: 200px;
    margin: 0;
    font-family: "Alegreya Sans SC", sans-serif;
    font-style: normal;
    font-size: 23px;
    line-height: 29px;
    letter-spacing: 1px;
  }
  .contact span { display: block; white-space: nowrap; }
  .slogan {
    margin: 0;
    font-family: "Pathway Gothic One", sans-serif;
    font-weight: 400;
    font-size: 80px;
    line-height: 1;
  }
  .slogan-line {
    position: absolute;
    white-space: nowrap;
  }
  .slogan-line.first { left: 34px; top: 92px; }
  .slogan-line.second { left: 94px; top: 194px; }
</style>
</head>
<body>
  <main class="sheet">
    <section class="card-front">
      <p class="brand-name">HALVARO</p>
      <p class="service-line">GPS AUDIO APPS</p>
      <address class="contact">
        <span>Mara Lindholt</span>
        <span>Am Lindenhang 7</span>
        <span>78999 Talheim-Musterau</span>
        <span>Tel.: +49 151 2408817</span>
        <span>Mail: mara.lindholt@halvaro-beispiel.de</span>
        <span>www.halvaro-beispiel.de</span>
      </address>
    </section>
    <div class="divider"></div>
    <section class="card-back">
      <p class="slogan">
        <span class="slogan-line first">Orte zum</span>
        <span class="slogan-line second">Sprechen bringen...</span>
      </p>
    </section>
  </main>
</body>
</html>
```